Quorvane - corporate Business Card

We need a good look and innovative business card for a new start up company based in Los Angeles called "Quorvane". We are in a payment business, including payment card, app, and ewallet. We are expert in online payment and Card not present (CNP) transaction.
We need an innovative, modern business card.

Our logo font is Aero Matics

Target Market(s)

Startup - Bank - Online Payment - Card Manufacturing

Industry/Entity Type

Startup

Contact Information for Business Card

phone: 424 555 0173 - Address: 4270 Marbrook blvd, Dunmere City, CA 90417

Requirements
Must have
• Message: innovative, professional, expert, high tech, trust, online payment expert, security
Nice to have
• no comment
Should not have
• no Comment

```html
<!DOCTYPE html>
<html lang="en">
<head>
<meta charset="utf-8">
<title>Quorvane – Business Card</title>
<link rel="stylesheet" href="https://fonts.googleapis.com/css2?family=Fira+Sans+Condensed:wght@400;500;600&display=swap">
<style>
  :root {
    --brand-red: #b8202f;
    --band-grey: #58585a;
    --text-grey: #4a4a4a;
    --card-white: #ffffff;
    --backdrop: #ececec;
  }
  * { margin: 0; padding: 0; box-sizing: border-box; }
  html, body {
    width: 1200px;
    height: 1200px;
    overflow: hidden;
    background: var(--backdrop);
    font-family: "Fira Sans Condensed", sans-serif;
  }
  .canvas { position: relative; width: 1200px; height: 1200px; }
  .card {
    position: absolute;
    left: 237px;
    width: 725px;
    height: 411px;
    overflow: hidden;
  }
  .card-front { top: 154px; background: var(--card-white); }
  .card-back { top: 634px; background: var(--brand-red); }
  .card-art { position: absolute; inset: 0; }

  .brand-name {
    position: absolute;
    font-weight: 600;
    line-height: 1;
    white-space: nowrap;
  }
  .front-brand { left: 134px; top: 62px; font-size: 50px; color: var(--brand-red); }
  .back-brand { left: 288px; top: 156px; font-size: 78px; color: var(--card-white); }

  .holder { position: absolute; right: 34px; text-align: right; }
  .holder-name { top: 148px; font-size: 25px; font-weight: 500; color: var(--brand-red); }
  .holder-title { top: 184px; font-size: 16px; color: var(--text-grey); }

  .address {
    position: absolute;
    left: 45px;
    top: 322px;
    font-size: 17px;
    line-height: 26px;
    color: var(--card-white);
    font-style: normal;
  }
  .contact-list {
    position: absolute;
    right: 32px;
    top: 303px;
    list-style: none;
    color: var(--card-white);
    font-size: 17px;
  }
  .contact-item {
    display: flex;
    justify-content: flex-end;
    align-items: center;
    gap: 10px;
    height: 28.5px;
  }
  .contact-icon { width: 18px; height: 18px; }

  .back-web {
    position: absolute;
    left: 288px;
    width: 290px;
    top: 246px;
    text-align: right;
    font-size: 16px;
    font-weight: 600;
    color: var(--card-white);
  }
</style>
</head>
<body>
<main class="canvas">

  <section class="card card-front" aria-label="Business card front">
    <svg class="card-art" width="725" height="411" viewBox="0 0 725 411" aria-hidden="true">
      <circle cx="81" cy="88" r="40" fill="var(--brand-red)"/>
      <polygon points="0,200 362,200 430,250 725,250 725,411 0,411" fill="var(--brand-red)"/>
      <polygon points="415,218 725,218 725,236 439,236" fill="var(--band-grey)"/>
    </svg>
    <span class="brand-name front-brand">Quorvane</span>
    <p class="holder holder-name">Daniel Reyes</p>
    <p class="holder holder-title">Managing Partner</p>
    <address class="address">4270 Marbrook blvd<br>Dunmere City, CA 90417</address>
    <ul class="contact-list">
      <li class="contact-item">424 555 0173
        <svg class="contact-icon" viewBox="0 0 24 24" aria-hidden="true"><path fill="#fff" d="M6.6 2.5l3 3.6-1.9 2.4c1.3 2.9 3.6 5.3 6.6 6.7l2.3-2 3.7 3-1.8 3.5C10.9 19.6 4.3 13 4 4.3z"/></svg>
      </li>
      <li class="contact-item">daniel@quorvane.com
        <svg class="contact-icon" viewBox="0 0 24 24" aria-hidden="true"><rect x="2.5" y="5" width="19" height="14" fill="none" stroke="#fff" stroke-width="1.8"/><path d="M2.5 5l9.5 8 9.5-8M2.5 19l7-6.5M21.5 19l-7-6.5" fill="none" stroke="#fff" stroke-width="1.6"/></svg>
      </li>
      <li class="contact-item">www.quorvane.com
        <svg class="contact-icon" viewBox="0 0 24 24" aria-hidden="true"><g fill="none" stroke="#fff" stroke-width="1.6"><circle cx="12" cy="12" r="9.5"/><ellipse cx="12" cy="12" rx="4" ry="9.5"/><path d="M2.5 12h19M4 7h16M4 17h16"/></g></svg>
      </li>
    </ul>
  </section>

  <section class="card card-back" aria-label="Business card back">
    <svg class="card-art" width="725" height="411" viewBox="0 0 725 411" aria-hidden="true">
      <circle cx="205" cy="203" r="66" fill="var(--card-white)"/>
    </svg>
    <span class="brand-name back-brand">Quorvane</span>
    <p class="back-web">www.quorvane.com</p>
  </section>

</main>
</body>
</html>
```